banner ad for a very high end interior designer

Our website only gets a small number of hits per day, but it is often people looking to choose designers to interview. We are going to do a Vornix remarketing campaign to show ads to people who have previously visited our website. The goal is to make sure they remember the quality and sophistication of our work.
The banner should include pictures of our work. You can see this at www.corinnevasquezdesign.example. Perhaps a single image per banner, or a slideshow within the banner?
The goal is to create awareness and to remind the former website visitor of our work. So it is important to include the logo from our website in the banner ad for visual anchoring and recall. As well, the banner graphics should be of a quality that would be used by Edmund Vaisey or Orla Fenwick or marlow sisters or vorda or Delvaro.
As for a 'call to action', we can offer "See Our Work in Person" or some simpler wording. If the person clicks on the banner, it will take them to a landing page where they can request free tickets to the Amberlane Interiors Gala home. We are designing one of the rooms at that open home event.
Size: either 300 x 250. May buy a second at 320 x 100

```html
<!DOCTYPE html>
<html lang="en">
<head>
<meta charset="utf-8">
<title>Corinne Vasquez – Display Banner Set</title>
<link rel="stylesheet" href="https://fonts.googleapis.com/css2?family=Arimo:wght@400;700&display=swap">
<style>
  :root {
    --page: #ffffff;
    --frame: #9a9a9a;
    --gold: #e2b744;
    --gold-deep: #d6a935;
    --ink-light: #ffffff;
    --logo-grey: #6b6b6b;
    --label: #222222;
    --cta-top: #ff7a3d;
    --cta-bottom: #f2541b;
    --cta-edge: #d9480f;
    --cta-dot: #8a2f10;
    --swoosh: #8c8c8c;
    --photo-navy: #2c3f6e;
    --photo-cream: #ece6dc;
    --photo-white: #f7f6f3;
  }
  * { box-sizing: border-box; margin: 0; padding: 0; }
  html, body { width: 1200px; height: 1200px; overflow: hidden; background: var(--page); }
  body { font-family: "Arimo", Arial, sans-serif; }

  .stage {
    position: absolute; left: 0; top: 0;
    width: 850px; height: 850px;
    transform: scale(1.41176); transform-origin: 0 0;
  }

  .banner {
    position: absolute; overflow: hidden;
    border: 1px solid var(--frame); background: var(--page);
  }
  .size-label {
    position: absolute; font-size: 15px; color: var(--label);
    text-align: center; width: 120px;
  }

  .brand {
    position: absolute; display: flex; align-items: center; justify-content: center;
    background: linear-gradient(#ffffff 40%, #e9e9e9);
  }
  .brand-name {
    font-weight: 400; font-size: 11px; letter-spacing: 1.6px;
    color: var(--logo-grey); white-space: nowrap;
  }

  .headline {
    position: absolute; background: var(--gold);
    color: var(--ink-light); font-weight: 700; text-align: center;
    display: flex; flex-direction: column; justify-content: center;
    text-shadow: 0 1px 1px rgba(120, 80, 0, .35);
    line-height: 1;
  }

  .photo {
    position: absolute;
    background:
      linear-gradient(90deg, var(--photo-navy) 0 30%, var(--photo-cream) 30% 58%, var(--photo-white) 58% 78%, var(--photo-navy) 78%);
  }
  .photo.tall {
    background:
      linear-gradient(180deg, var(--photo-cream) 0 40%, var(--photo-white) 40% 75%, #d9d6d0 75%),
      var(--photo-cream);
  }
  .swoosh { position: absolute; }

  .cta {
    position: absolute; width: 134px; height: 35px;
    background: linear-gradient(var(--cta-top), var(--cta-bottom));
    border: 1px solid var(--cta-edge);
    box-shadow: 0 2px 3px rgba(0,0,0,.3);
    display: flex; align-items: center; justify-content: space-between;
    padding: 0 6px 0 7px;
  }
  .cta-text {
    color: var(--ink-light); font-weight: 700; font-size: 10.5px;
    text-shadow: 0 1px 1px rgba(0,0,0,.3); white-space: nowrap;
  }
  .cta-icon { width: 26px; height: 26px; }
</style>
</head>
<body>
<div class="stage">

  <!-- Leaderboard 728x90 -->
  <div class="banner leaderboard" style="left:69px; top:55px; width:728px; height:90px;">
    <div class="brand" style="left:0; top:0; width:168px; height:88px;">
      <span class="brand-name">CORINNE VASQUEZ</span>
    </div>
    <div class="headline" style="left:168px; top:0; width:186px; height:88px; font-size:18px;">
      <span>DO YOU NEED</span>
      <span>INTERIOR</span>
      <span style="font-size:16.5px;">ARCHITECTURE</span>
      <span style="font-size:16.5px;">SERVICES?</span>
    </div>
    <div class="photo" role="img" aria-label="Interior photograph: navy curved sofa, white bed with navy throw, blue curtains" style="left:354px; top:0; width:300px; height:88px;"></div>
    <svg class="swoosh" style="left:560px; top:0;" width="166" height="88" viewBox="0 0 166 88">
      <path d="M60 0 C110 20 110 68 60 88 L166 88 L166 0 Z" fill="#ffffff"/>
      <path d="M60 0 C110 20 110 68 60 88" fill="none" stroke="var(--swoosh)" stroke-width="4"/>
    </svg>
    <a class="cta" style="left:585px; top:32px;">
      <span class="cta-text">SEE OUR WORK</span>
      <svg class="cta-icon" viewBox="0 0 26 26"><circle cx="13" cy="13" r="12" fill="var(--cta-dot)"/><path d="M10 7.5 L18 13 L10 18.5 Z" fill="#ffffff"/></svg>
    </a>
  </div>
  <div class="size-label" style="left:355px; top:153px;">728X90</div>

  <!-- Medium rectangle 300x250 -->
  <div class="banner rectangle" style="left:69px; top:292px; width:300px; height:250px;">
    <div class="brand" style="left:0; top:0; width:298px; height:55px;">
      <span class="brand-name">CORINNE VASQUEZ</span>
    </div>
    <div class="headline" style="left:0; top:55px; width:298px; height:56px; font-size:19px;">
      <span>DO YOU NEED INTERIOR</span>
      <span>ARCHITECTUTE SERVICES?</span>
    </div>
    <div class="photo" role="img" aria-label="Interior photograph: navy curved sofa, white bed with navy throw, blue curtains" style="left:0; top:111px; width:298px; height:95px;"></div>
    <svg class="swoosh" style="left:0; top:160px;" width="298" height="88" viewBox="0 0 298 88">
      <path d="M0 10 C90 48 210 48 298 10 L298 88 L0 88 Z" fill="#ffffff"/>
      <path d="M0 10 C90 48 210 48 298 10" fill="none" stroke="var(--swoosh)" stroke-width="5"/>
    </svg>
    <a class="cta" style="left:83px; top:209px;">
      <span class="cta-text">SEE OUR WORK</span>
      <svg class="cta-icon" viewBox="0 0 26 26"><circle cx="13" cy="13" r="12" fill="var(--cta-dot)"/><path d="M10 7.5 L18 13 L10 18.5 Z" fill="#ffffff"/></svg>
    </a>
  </div>
  <div class="size-label" style="left:154px; top:552px;">300X250</div>

  <!-- Skyscraper 160x600 -->
  <div class="banner skyscraper" style="left:635px; top:208px; width:160px; height:600px;">
    <div class="brand" style="left:0; top:0; width:158px; height:80px;">
      <span class="brand-name" style="font-size:10px; letter-spacing:1.2px;">CORINNE VASQUEZ</span>
    </div>
    <div class="headline" style="left:0; top:80px; width:158px; height:178px; font-size:26px; line-height:1.08;">
      <span>DO YOU</span>
      <span>NEED</span>
      <span>INTERIOR</span>
      <span style="font-size:17px; margin-top:4px;">ARCHITECTUTE</span>
      <span style="font-size:24px; margin-top:2px;">SERVICES?</span>
    </div>
    <div class="photo tall" role="img" aria-label="Interior photograph: blue curtains by a window, white sofa and bed with navy throw" style="left:0; top:258px; width:158px; height:280px;"></div>
    <svg class="swoosh" style="left:0; top:488px;" width="158" height="110" viewBox="0 0 158 110">
      <path d="M0 20 C50 48 110 48 158 20 L158 110 L0 110 Z" fill="#ffffff"/>
      <path d="M0 20 C50 48 110 48 158 20" fill="none" stroke="var(--swoosh)" stroke-width="5"/>
    </svg>
    <a class="cta" style="left:12px; top:548px;">
      <span class="cta-text">SEE OUR WORK</span>
      <svg class="cta-icon" viewBox="0 0 26 26"><circle cx="13" cy="13" r="12" fill="var(--cta-dot)"/><path d="M10 7.5 L18 13 L10 18.5 Z" fill="#ffffff"/></svg>
    </a>
  </div>
  <div class="size-label" style="left:655px; top:817px;">160X600</div>

</div>
</body>
</html>
```